Franchise Vacation Rental Company Website

We are looking for fresh, new and creative design ideas to help enhance this site. We are a vacation rental company that is starting a new franchise business. This will be our home franchise page, and will need to appeal to franchise candidates as well as travelers looking for vacation homes in our current locations.

Business

```html
<!DOCTYPE html>
<html lang="en">
<head>
<meta charset="utf-8">
<title>BrightHaven – Vacation Rentals &amp; Franchise</title>
<link rel="stylesheet" href="https://fonts.googleapis.com/css2?family=Open+Sans:ital,wght@0,400;0,600;0,700;1,700&display=swap">
<style>
:root{
  --gutter:#333333;
  --topbar:#2a2a2a;
  --navy:#163a6e;
  --navy-deep:#0f2b57;
  --blue:#1e6fb5;
  --blue-light:#3aa2e6;
  --lime:#a9c83a;
  --lime-dark:#8fae27;
  --panel:#c9c9c9;
  --panel-light:#d6d6d6;
  --ink:#1b1b1b;
  --white:#ffffff;
  --muted:#bdbdbd;
}
*{box-sizing:border-box;margin:0;padding:0}
html,body{width:748px;height:1200px;overflow:hidden}
body{background:var(--gutter);font-family:"Open Sans",Arial,sans-serif;color:var(--ink)}
.page{width:748px;height:1200px;position:relative}
.column{width:592px;margin:0 auto}

.topbar{height:20px;background:var(--topbar);border-bottom:1px solid var(--blue)}
.topbar .column{display:flex;justify-content:space-between;align-items:center;height:20px;font-size:10px;color:var(--muted);font-weight:600}

.site-header{height:72px;background:linear-gradient(90deg,var(--navy-deep) 0%,var(--blue) 45%,var(--navy-deep) 100%);border-bottom:1px solid var(--blue-light)}
.site-header .column{height:72px;display:flex;align-items:center;justify-content:space-between}
.brand{display:flex;align-items:center;gap:8px;color:var(--lime);font-size:31px;font-weight:400;letter-spacing:-.5px}
.brand-dot{width:12px;height:12px;border-radius:50%;background:var(--lime)}
.main-nav{display:flex;gap:0;font-size:13px;font-weight:600;color:var(--white)}
.main-nav span{padding:0 16px;border-left:1px solid var(--white);line-height:13px}
.main-nav span:first-child{border-left:none}
.main-nav span:last-child{padding-right:0}

.hero{height:176px;margin-top:2px;background:linear-gradient(180deg,#6fb6e8 0%,#9fd6f0 30%,#22c3c9 55%,#e8dcc2 78%,#d8c7a6 100%)}
.section-nav{height:30px;background:var(--navy);border:1px solid var(--blue-light);display:flex;justify-content:center;align-items:center;font-size:12px;font-weight:600;color:var(--white)}
.section-nav span{padding:0 28px;border-left:2px solid var(--white);line-height:12px}
.section-nav span:first-child{border-left:none}
.nav-shadow{height:4px;background:#222}

.destinations{background:var(--panel);padding:16px 36px 12px;display:grid;grid-template-columns:248px 248px;column-gap:32px;row-gap:14px}
.destination-photo{height:172px;border:3px solid var(--lime);background:var(--white);padding:5px;border-radius:3px}
.destination-photo div{width:100%;height:100%}
.photo-map{background:linear-gradient(135deg,#a9c8e8 0%,#cfe0c0 40%,#a9c8e8 70%,#e2ddc7 100%)}
.photo-beach{background:linear-gradient(180deg,#5ea4dc 0%,#bfe0f2 38%,#3fc0c8 55%,#efe6d2 72%,#d9c9aa 100%)}
.photo-ship{background:linear-gradient(180deg,#4d9ad8 0%,#a6d2ef 45%,#f2f2f2 62%,#2fb8c0 78%,#1b8f9a 100%)}
.photo-canal{background:linear-gradient(135deg,#c9a77f 0%,#e6d2b2 35%,#8c9a7a 65%,#c04a3a 100%)}
.destination-label{margin-top:9px;height:31px;background:var(--navy);border:1px solid var(--blue-light);border-radius:3px;display:flex;align-items:center;gap:10px;padding-left:10px;color:var(--white);font-size:16px;font-weight:700}

.discover{background:var(--panel);display:flex;padding:6px 10px 12px 18px;gap:24px}
.discover-text{width:286px}
.discover-text h2{font-size:13px;font-weight:700;color:var(--navy);margin-bottom:2px}
.discover-text p{font-size:8px;line-height:10.5px;font-weight:700;margin-bottom:2px}
.signup{display:flex;gap:10px;margin-top:10px}
.signup-field{width:186px;height:18px;background:var(--white);border:1px solid var(--blue)}
.signup-button{width:60px;height:18px;background:linear-gradient(180deg,var(--blue-light),var(--navy));border:1px solid var(--navy-deep);color:var(--white);font-size:8px;font-weight:600;display:flex;align-items:center;justify-content:center}

.promo{position:relative;width:288px;height:152px;background:var(--lime);margin-top:6px;padding:10px 0 0 30px}
.promo::before{content:"";position:absolute;left:-22px;top:0;border-top:0 solid transparent;border-right:22px solid var(--lime);border-bottom:22px solid transparent}
.promo-item{display:flex;align-items:center;gap:14px;height:46px;color:var(--navy);font-size:13px;font-weight:700;font-style:italic}
.promo-item svg{flex:none}

.footer-band{height:30px;margin-top:6px;background:linear-gradient(90deg,var(--navy-deep) 0%,var(--blue) 50%,var(--navy-deep) 100%);border:1px solid var(--blue-light)}
.footer-columns{background:var(--panel);display:flex;justify-content:space-between;padding:8px 20px 18px 20px}
.footer-col{width:124px}
.footer-col h3{font-size:12px;font-weight:700;color:var(--navy);margin-bottom:2px}
.footer-col p{font-size:8px;line-height:10.5px;font-weight:700}
.footer-strip{height:26px;background:var(--panel-light)}
</style>
</head>
<body>
<div class="page">
  <div class="topbar">
    <div class="column">
      <span>1.800.555.0142 [1.800.555.0143]</span>
      <span>hello@brighthaven-stays.com</span>
    </div>
  </div>

  <header class="site-header">
    <div class="column">
      <div class="brand"><span>BrightHaven</span><span class="brand-dot"></span></div>
      <nav class="main-nav"><span>Home</span><span>Your Property</span><span>Contact Us</span></nav>
    </div>
  </header>

  <div class="column">
    <div class="hero" role="img" aria-label="Photo of a couple relaxing in beach chairs on a tropical white-sand beach with turquoise water"></div>
    <nav class="section-nav"><span>Bright Haven</span><span>Franchise</span><span>Philosophy</span><span>News</span></nav>
    <div class="nav-shadow"></div>

    <section class="destinations">
      <div class="destination">
        <div class="destination-photo"><div class="photo-map" role="img" aria-label="World map showing rental locations"></div></div>
        <div class="destination-label"><svg width="16" height="18" viewBox="0 0 16 18"><path d="M8 1a6 6 0 0 0-6 6c0 4.5 6 10 6 10s6-5.5 6-10a6 6 0 0 0-6-6z" fill="none" stroke="#a9c83a" stroke-width="2"/><circle cx="8" cy="7" r="2" fill="#a9c83a"/></svg>FIND YOUR HAVEN!</div>
      </div>
      <div class="destination">
        <div class="destination-photo"><div class="photo-beach" role="img" aria-label="Photo of beach chairs on a sunny Bora Bora beach"></div></div>
        <div class="destination-label"><svg width="16" height="18" viewBox="0 0 16 18"><path d="M8 1a6 6 0 0 0-6 6c0 4.5 6 10 6 10s6-5.5 6-10a6 6 0 0 0-6-6z" fill="none" stroke="#a9c83a" stroke-width="2"/><circle cx="8" cy="7" r="2" fill="#a9c83a"/></svg>BORA BORA</div>
      </div>
      <div class="destination">
        <div class="destination-photo"><div class="photo-ship" role="img" aria-label="Photo of a cruise ship near a palm-lined Miami shore"></div></div>
        <div class="destination-label"><svg width="16" height="18" viewBox="0 0 16 18"><path d="M8 1a6 6 0 0 0-6 6c0 4.5 6 10 6 10s6-5.5 6-10a6 6 0 0 0-6-6z" fill="none" stroke="#a9c83a" stroke-width="2"/><circle cx="8" cy="7" r="2" fill="#a9c83a"/></svg>MIAMI</div>
      </div>
      <div class="destination">
        <div class="destination-photo"><div class="photo-canal" role="img" aria-label="Photo of travellers on a gondola ride along a Venice canal"></div></div>
        <div class="destination-label"><svg width="16" height="18" viewBox="0 0 16 18"><path d="M8 1a6 6 0 0 0-6 6c0 4.5 6 10 6 10s6-5.5 6-10a6 6 0 0 0-6-6z" fill="none" stroke="#a9c83a" stroke-width="2"/><circle cx="8" cy="7" r="2" fill="#a9c83a"/></svg>VENECIA</div>
      </div>
    </section>

    <section class="discover">
      <div class="discover-text">
        <h2>Ready to Discover</h2>
        <p>Set out on a fresh journey with homes chosen for comfort, light and easy access to the best beaches, markets and old town streets in each region.</p>
        <p>Owners join a trusted network, share local know-how and welcome guests who come back year after year to the places they love most.</p>
        <div class="signup"><div class="signup-field"></div><div class="signup-button">Sign me up</div></div>
      </div>
      <div class="promo">
        <div class="promo-item"><svg width="26" height="30" viewBox="0 0 26 30"><path d="M13 2a10 10 0 0 0-10 10c0 8 10 16 10 16s10-8 10-16A10 10 0 0 0 13 2z" fill="none" stroke="#fff" stroke-width="2.5"/><circle cx="13" cy="12" r="3.5" fill="#fff"/></svg>Know of a Haven?</div>
        <div class="promo-item"><svg width="30" height="28" viewBox="0 0 30 28"><circle cx="10" cy="7" r="5" fill="#fff"/><path d="M1 24c0-6 4-9 9-9s9 3 9 9z" fill="#fff"/><circle cx="21" cy="11" r="4.5" fill="#fff"/><path d="M13 27c0-5 3.5-8 8-8s8 3 8 8z" fill="#fff"/></svg>Spot travels free!</div>
        <div class="promo-item"><svg width="26" height="26" viewBox="0 0 26 26"><circle cx="13" cy="13" r="11" fill="none" stroke="#fff" stroke-width="2.5"/><path d="M13 6v7l-5 4" fill="none" stroke="#fff" stroke-width="2.5" stroke-linecap="round"/></svg>Last Minute Deals!</div>
      </div>
    </section>

    <div class="footer-band"></div>
    <footer class="footer-columns">
      <div class="footer-col"><h3>Bright Haven</h3><p>Homes by the sea and in the city, each one checked and ready for you.</p></div>
      <div class="footer-col"><h3>Contact Us</h3><p>Write or call our team any day of the week for help with your stay.</p></div>
      <div class="footer-col"><h3>Franchise</h3><p>Open a branch in your own town with our tools, training and support.</p></div>
    </footer>
    <div class="footer-strip"></div>
  </div>
</div>
</body>
</html>
```